Web Redesign

Hi,
We have a created a webpage on plumleaf using a theme called Tavor which can be downloaded at Skin Harbour which we like the look and feel of.

You can view our current page we are building at:: www.pledgeport-example.com.au

The text needs altering which we will do ourselves. Basically, we are requiring the graphic elements that should be placed on EACh page.

The webpage we like the look and feel of is:
http://www.brightcog-example.com.au/
http://www.kelvo-example.com.au/

Ideas for pages:
Our process - could be something along the lines of http://www.kelvo-example.com.au/our-method
Our service - could be something along the lines of http://www.brightcog-example.com.au/iphone-application-development/
Our work - could be something along the lines of http://www.kelvo-example.com.au/our-work
Our Value Proposition - could be something along hte lines of http://www.brightcog-example.com.au/services/
About Us - happy to go with your suggestion
Contact us - happy to use what we have currently if you can come up with a suitable graphic http://pledgeport-example.com.au/contact-example-1/
FAQ - happy to use what we have currently if you can come up with a suitable graphic http://pledgeport-example.com.au/contact-example-1/

We would like you to come up with the design/graphics and add then once the winner of the project is chosen we could give you the admin login details to upload the images or we could do it ourselves if you supplied them all and in which case would be good to know where you envision they would be placed.

To give you some insight, this is a branch from business we have called TideMoss (www.tidemoss-example.org) where we aggregate charities onto the one platform for smart phones and allow people to donate to their favourite charity anywhere, anytime with the push of a button.
Pledgeport is a side business to this where we have began building white labelled apps for charities on our TideMoss platform and we wanted a separate webpage for this.

Once this webpage is completed, we would love to get the TideMoss webpage revamped so there is further opportunity to work with you on this project.

Happy to answer any questions if needed.

Thanks and look forward to seeing the designs
Updates

Our Ideas for pages:

Target Market(s)

Charities, corporates

Industry/Entity Type

Building

```html
<!DOCTYPE html>
<html lang="en">
<head>
<meta charset="utf-8">
<title>TideMoss – Branded Charity Apps</title>
<link href="https://fonts.googleapis.com/css2?family=Open+Sans:ital,wght@0,400;0,600;0,700;0,800;1,400&family=Oswald:wght@500;700&display=swap" rel="stylesheet">
<style>
  :root{
    --blue:#1f8fd3;
    --blue-dark:#146fae;
    --orange:#f3a21b;
    --orange-dark:#d9860b;
    --ink:#3a3d42;
    --text:#7a7d82;
    --muted:#a5a8ad;
    --line:#e3e4e6;
    --paper:#ffffff;
    --hero-a:#b7bcc2;
    --hero-b:#6f767e;
    --footer:#3b3e44;
    --footer-deep:#2e3035;
    --yellow:#ffd23a;
  }
  *{box-sizing:border-box;margin:0;padding:0}
  html,body{width:814px;height:1200px;overflow:hidden}
  body{position:relative;background:var(--paper);font-family:"Open Sans",Arial,sans-serif;color:var(--text)}

  /* header */
  .site-header{position:absolute;left:0;top:0;width:814px;height:80px;background:var(--paper);border-bottom:1px solid var(--line)}
  .brand{position:absolute;left:30px;top:10px;display:flex;align-items:center;gap:8px}
  .brand-dot{width:26px;height:26px;border-radius:50%;background:var(--blue)}
  .brand-name{font-size:24px;font-weight:700;color:var(--blue);letter-spacing:-.5px}
  .header-phone{position:absolute;right:30px;top:16px;display:flex;align-items:center;gap:6px;font-size:13px;color:var(--ink);font-weight:600}
  .main-nav{position:absolute;left:30px;top:52px;display:flex;gap:0}
  .main-nav a{display:block;padding:6px 10px 8px;font-size:10px;font-weight:700;color:var(--ink);text-decoration:none;letter-spacing:.3px}
  .main-nav a.is-active{color:var(--blue);border-bottom:3px solid var(--blue)}

  /* hero */
  .hero{position:absolute;left:0;top:80px;width:814px;height:330px;overflow:hidden}
  .hero-backdrop{position:absolute;inset:0;background:radial-gradient(ellipse at 30% 40%,var(--hero-a),var(--hero-b))}
  .hero-title{position:absolute;left:40px;top:70px;width:380px;color:#fff;font-size:25px;line-height:1.3;font-weight:700;text-shadow:0 1px 3px rgba(0,0,0,.35)}
  .store-button{position:absolute;left:110px;top:200px;width:180px;height:46px;border-radius:5px;background:linear-gradient(var(--orange),var(--orange-dark));border:1px solid #c07608;display:flex;align-items:center;gap:10px;padding:0 12px;color:#fff;box-shadow:0 2px 4px rgba(0,0,0,.3)}
  .store-button .badge{width:24px;height:24px;border-radius:4px;background:rgba(255,255,255,.85)}
  .store-button small{display:block;font-size:9px}
  .store-button strong{display:block;font-size:14px;line-height:1.1}
  .hero-devices{position:absolute;left:440px;top:25px;width:340px;height:260px;border-radius:14px;background:linear-gradient(150deg,#2b2f35,#565d66 60%,#dfe3e7);box-shadow:0 10px 25px rgba(0,0,0,.35)}
  .hero-edge{position:absolute;left:0;bottom:-1px}

  /* app section */
  .app-intro{position:absolute;left:30px;top:440px;width:365px}
  .section-heading{font-size:17px;line-height:1.25;font-weight:700;color:var(--orange);text-transform:uppercase}
  .app-intro p{margin-top:12px;font-size:11px;line-height:1.7}
  .read-more{display:inline-block;margin-top:14px;padding:4px 12px;font-size:10px;color:var(--ink);background:#f1f2f3;border:1px solid var(--line);border-radius:3px}

  .services{position:absolute;left:425px;top:432px;width:355px;height:210px;background:var(--blue);border-radius:3px;color:#fff}
  .services h2{font-size:15px;font-weight:700;padding:12px 16px;border-bottom:1px solid rgba(255,255,255,.3)}
  .services-photo{position:absolute;left:16px;top:56px;width:150px;height:130px;background:linear-gradient(135deg,#cfd8df,#8fa3b2)}
  .services-copy{position:absolute;left:180px;top:58px;width:160px}
  .services-copy h3{font-size:13px;font-weight:700;line-height:1.3}
  .services-copy p{margin-top:6px;font-size:10px;line-height:1.6;color:#dbeefa}
  .slider-arrow{position:absolute;top:108px;width:20px;height:20px;border-radius:50%;background:var(--ink);display:flex;align-items:center;justify-content:center}
  .slider-arrow.prev{left:-10px}
  .slider-arrow.next{right:-10px}

  .divider{position:absolute;left:30px;width:754px;height:1px;background:var(--line)}

  /* testimonials & sponsors */
  .testimonials{position:absolute;left:30px;top:700px;width:365px}
  .block-heading{font-size:15px;font-weight:800;color:var(--ink);letter-spacing:.5px}
  .quote{position:relative;margin-top:14px;padding-left:30px;font-style:italic;font-size:11px;line-height:1.7}
  .quote::before{content:"\201C";position:absolute;left:0;top:-14px;font-size:44px;color:var(--line);font-style:normal}
  .quote cite{display:block;margin-top:8px;font-size:10px;color:var(--muted)}
  .sponsors{position:absolute;left:425px;top:700px;width:355px}
  .sponsor-grid{margin-top:14px;display:grid;grid-template-columns:repeat(3,1fr);gap:14px 16px}
  .sponsor-mark{height:36px;background:#e9eaec;border-radius:2px}
  .sponsor-mark.wide{grid-column:span 2;height:40px}

  /* banner */
  .promo{position:absolute;left:30px;top:878px;width:754px;height:76px;border-radius:4px;background:linear-gradient(var(--blue),var(--blue-dark));overflow:hidden}
  .promo-photo{position:absolute;left:0;top:0;width:110px;height:76px;background:linear-gradient(135deg,#9bd1ee,#3d7fa8)}
  .promo-copy{position:absolute;left:130px;top:12px;font-family:"Oswald",sans-serif;text-transform:uppercase}
  .promo-copy .lead{font-size:20px;font-weight:700;color:var(--yellow);line-height:1.1}
  .promo-copy .lead span{font-family:"Open Sans",sans-serif;font-size:10px;color:#fff;font-weight:600;text-transform:none}
  .promo-copy .tag{font-size:22px;font-weight:700;color:#fff;line-height:1.2}
  .promo-cta{position:absolute;right:10px;top:9px;width:150px;height:58px;background:#fff;border-radius:3px;font-family:"Oswald",sans-serif;font-weight:700;font-size:20px;line-height:1;color:var(--blue);text-align:center;padding-top:8px}

  /* address */
  .address{position:absolute;left:30px;top:972px;width:754px}
  .address h2{font-size:14px;font-weight:800;color:var(--ink)}
  .address-row{margin-top:10px;display:flex;align-items:center;justify-content:space-between}
  .address-item{display:flex;align-items:center;gap:8px;font-size:11px;color:var(--ink)}
  .address-item.email{font-size:14px;color:var(--blue)}
  .address-item.phone{font-size:17px;color:var(--blue)}
  .icon-chip{width:26px;height:26px;border-radius:50%;background:var(--blue);display:flex;align-items:center;justify-content:center}

  /* footer */
  .site-footer{position:absolute;left:0;top:1040px;width:814px;height:160px;background:var(--footer)}
  .footer-edge{position:absolute;left:0;top:-1px}
  .tweet-box{position:absolute;left:30px;top:28px;width:365px;height:66px;background:var(--blue);border-radius:3px;display:flex;align-items:center;gap:12px;padding:0 14px}
  .tweet-dot{flex:none;width:36px;height:36px;border-radius:50%;background:#fff}
  .tweet-box p{font-size:10px;line-height:1.5;color:#fff}
  .tweet-box p span{display:block;color:#cde8f8;font-size:9px}
  .newsletter{position:absolute;left:425px;top:24px;width:355px}
  .newsletter h2{font-size:14px;font-weight:700;color:#fff}
  .newsletter p{margin-top:4px;font-size:10px;line-height:1.5;color:#b5b8bd;width:270px}
  .signup{margin-top:8px;display:flex;align-items:center;gap:0}
  .signup .field{width:200px;height:24px;background:#fff;border-radius:2px 0 0 2px;font-size:10px;color:var(--muted);padding:5px 8px}
  .signup .go{width:34px;height:24px;background:var(--footer-deep);border-radius:0 2px 2px 0;color:#fff;font-size:10px;text-align:center;padding-top:5px}
  .social{position:absolute;right:0;top:0;display:flex;gap:6px}
  .social span{width:20px;height:20px;border-radius:2px;background:#55595f}
  .footer-links{position:absolute;left:30px;top:114px;font-size:10px;color:#c9ccd0}
  .footer-links a{color:#c9ccd0;text-decoration:none}
  .copyright{position:absolute;left:30px;top:134px;font-size:9px;color:#8e9298}
</style>
</head>
<body>

<header class="site-header">
  <div class="brand"><span class="brand-dot"></span><span class="brand-name">TideMoss</span></div>
  <div class="header-phone">
    <svg width="14" height="14" viewBox="0 0 24 24"><path fill="#1f8fd3" d="M6.6 10.8a15 15 0 0 0 6.6 6.6l2.2-2.2c.3-.3.7-.4 1-.2 1.1.4 2.3.6 3.6.6.6 0 1 .4 1 1V20c0 .6-.4 1-1 1A17 17 0 0 1 3 4c0-.6.4-1 1-1h3.5c.6 0 1 .4 1 1 0 1.2.2 2.4.6 3.6.1.3 0 .7-.2 1z"/></svg>
    +0100 555 019
  </div>
  <nav class="main-nav">
    <a class="is-active" href="#">HOME</a>
    <a href="#">ABOUT</a>
    <a href="#">OUR PROCESS</a>
    <a href="#">OUR SERVICES</a>
    <a href="#">OUR WORK</a>
    <a href="#">OUR VALUE PROPOSITION</a>
    <a href="#">FAQ</a>
    <a href="#">CONTACT</a>
  </nav>
</header>

<section class="hero">
  <div class="hero-backdrop" role="img" aria-label="Soft-focus photo of people using mobile phones"></div>
  <h1 class="hero-title">TideMoss is a social enterprise empowering mobile users to connect and donate...</h1>
  <a class="store-button" href="#"><span class="badge"></span><span><small>Available on the</small><strong>TideMoss</strong></span></a>
  <div class="hero-devices" role="img" aria-label="Smartphone and tablet showing the donation app screens"></div>
  <svg class="hero-edge" width="814" height="16" viewBox="0 0 814 16" preserveAspectRatio="none">
    <path fill="#ffffff" d="M0 8 L30 4 L62 10 L95 5 L130 11 L168 6 L205 10 L240 3 L280 9 L318 5 L355 11 L395 6 L430 10 L470 4 L510 9 L548 5 L590 11 L628 6 L665 10 L705 4 L742 9 L780 5 L814 9 L814 16 L0 16 Z"/>
  </svg>
</section>

<section class="app-intro">
  <h2 class="section-heading">The app - branded with your organisation's name and logo</h2>
  <p>Your charity gets its own app, carrying your name, colours and logo, built on our proven giving platform. Supporters can donate in seconds from anywhere, at any time, with a single tap. We handle the build, testing and store release so your team can stay focused on the cause, while every gift reaches you quickly and securely.</p>
  <span class="read-more">Read More</span>
</section>

<section class="services">
  <h2>OUR SERVICES</h2>
  <div class="services-photo" role="img" aria-label="Photo of a supporter donating by phone"></div>
  <div class="services-copy">
    <h3>Receive Donations Immediately</h3>
    <p>Gifts made through your app arrive fast, with clear reports on every supporter and campaign.</p>
  </div>
  <span class="slider-arrow prev"><svg width="8" height="10" viewBox="0 0 8 10"><path d="M6 1 L2 5 L6 9" stroke="#fff" stroke-width="2" fill="none"/></svg></span>
  <span class="slider-arrow next"><svg width="8" height="10" viewBox="0 0 8 10"><path d="M2 1 L6 5 L2 9" stroke="#fff" stroke-width="2" fill="none"/></svg></span>
</section>

<div class="divider" style="top:680px"></div>

<section class="testimonials">
  <h2 class="block-heading">TESTIMONIALS</h2>
  <blockquote class="quote">Our supporters love how simple it is to give. The branded app raised more in its first month than we hoped for the whole year.
    <cite>- Sam Carter</cite>
  </blockquote>
</section>

<section class="sponsors">
  <h2 class="block-heading">SPONSORS</h2>
  <div class="sponsor-grid">
    <span class="sponsor-mark"></span>
    <span class="sponsor-mark"></span>
    <span class="sponsor-mark"></span>
    <span class="sponsor-mark wide"></span>
  </div>
</section>

<aside class="promo">
  <div class="promo-photo" role="img" aria-label="Hand holding a phone with a charity app"></div>
  <div class="promo-copy">
    <div class="lead">On time. On budget. <span>Done in time to start fundraising</span></div>
    <div class="tag">We care about not-for-profits.</div>
  </div>
  <div class="promo-cta">HELP ME<br>GO MOBILE</div>
</aside>

<div class="divider" style="top:964px"></div>

<section class="address">
  <h2>ADDRESS:</h2>
  <div class="address-row">
    <div class="address-item">
      <span class="icon-chip"><svg width="12" height="14" viewBox="0 0 12 16"><path fill="#fff" d="M6 0a6 6 0 0 0-6 6c0 4.5 6 10 6 10s6-5.5 6-10a6 6 0 0 0-6-6zm0 8.5A2.5 2.5 0 1 1 6 3.5a2.5 2.5 0 0 1 0 5z"/></svg></span>
      Post Office Box 001, Lorem Ipsum, City Name, Country 2007
    </div>
    <div class="address-item email">
      <span class="icon-chip"><svg width="14" height="10" viewBox="0 0 14 10"><rect x=".5" y=".5" width="13" height="9" fill="none" stroke="#fff"/><path d="M.5 .5 L7 6 L13.5 .5" fill="none" stroke="#fff"/></svg></span>
      info@tidemoss-example.org
    </div>
    <div class="address-item phone">
      <span class="icon-chip"><svg width="13" height="13" viewBox="0 0 24 24"><path fill="#fff" d="M6.6 10.8a15 15 0 0 0 6.6 6.6l2.2-2.2c.3-.3.7-.4 1-.2 1.1.4 2.3.6 3.6.6.6 0 1 .4 1 1V20c0 .6-.4 1-1 1A17 17 0 0 1 3 4c0-.6.4-1 1-1h3.5c.6 0 1 .4 1 1 0 1.2.2 2.4.6 3.6.1.3 0 .7-.2 1z"/></svg></span>
      100 555 0190
    </div>
  </div>
</section>

<footer class="site-footer">
  <svg class="footer-edge" width="814" height="12" viewBox="0 0 814 12" preserveAspectRatio="none">
    <path fill="#ffffff" d="M0 0 L814 0 L814 5 L775 9 L738 4 L700 8 L660 3 L622 9 L585 5 L545 10 L505 4 L468 8 L430 3 L392 9 L352 5 L315 10 L275 4 L238 8 L200 3 L160 9 L122 5 L85 10 L45 4 L0 8 Z"/>
  </svg>
  <div class="tweet-box">
    <span class="tweet-dot"></span>
    <p>Another local shelter just launched its own giving app with us. Proud to help them grow.<span>2 days ago</span></p>
  </div>
  <div class="newsletter">
    <h2>Newsletter!</h2>
    <p>Sign up for news, app launches and tips on mobile fundraising.</p>
    <div class="signup"><span class="field">Enter your email</span><span class="go">Go</span></div>
    <div class="social"><span></span><span></span></div>
  </div>
  <nav class="footer-links">
    <a href="#">Home</a> | <a href="#">About</a> | <a href="#">Our Process</a> | <a href="#">Our Services</a> | <a href="#">Our Work</a> | <a href="#">Our Value Proposition</a> | <a href="#">FAQ</a> | <a href="#">Contact</a>
  </nav>
  <p class="copyright">Copyright © 2013 TideMoss. All Rights Reserved.</p>
</footer>

</body>
</html>
```